Business Card Project for Firm Deck Hoisting

Business name is "Firm Deck Hoisting" we are a scaffolding & rigging business specialising in local and remote work for:
- scaffolding (residential, commercial, industrial)
- rigging
-man material hoists
- swing stages
- labour hire

On the back of the card I would like FDH as the symbol / logo. I have attached the logos we have had created by sketch harbour. We would like to use bold colours – preferably as the same colour scheme as the logo.

Target Market(s)

Construction business

Industry/Entity Type

Construction

Contact Information for Business Card

name: Owen Pellew
Title: Director
Phone: 0491 572 864
Address: PO BOX 3251, Elmsvale SA 5190
Email: owen@firmdeckhoisting.com.au
Website: www.firmdeckhoisting.com.au

Font styles to use
Sans Serif

Requirements
Must have
• Must use existing logo & prefering using bold colours
Nice to have
• Would be nice to have a line of dot points in what we specialise in but not essential
• Would be nice to see some designs with a slogan but not essential
Should not have
• NA

```html
<!DOCTYPE html>
<html lang="en">
<head>
<meta charset="utf-8">
<title>Firm Deck Hoisting – Business Card Concepts</title>
<link href="https://fonts.googleapis.com/css2?family=Roboto:wght@400;500;700&display=swap" rel="stylesheet">
<style>
  :root{
    --blue:#1177bd;
    --black:#000;
    --white:#fff;
    --ink:#111;
    --grey-top:#ececec;
    --grey-bottom:#ffffff;
  }
  *{box-sizing:border-box;margin:0;padding:0}
  html,body{width:1199px;height:1200px;overflow:hidden;background:var(--white)}
  body{position:relative;font-family:"Roboto",Arial,sans-serif;color:var(--ink)}
  .icon-defs{position:absolute;width:0;height:0}

  .card{position:absolute;width:519px;height:359px;overflow:hidden;background:var(--white);
        border-top:4px solid var(--black);border-bottom:5px solid var(--black)}
  .card--split{left:44px;top:38px}
  .card--bars{left:44px;top:422px}
  .card--diagonal{left:44px;top:808px;background:linear-gradient(180deg,var(--grey-top),var(--grey-bottom))}

  .brand{position:absolute;display:flex;align-items:center;gap:8px;white-space:nowrap}
  .brand__mark{width:.9em;height:.9em;background:var(--blue);flex:none}
  .brand__name{font-weight:700;color:var(--ink);letter-spacing:.5px}

  /* split card */
  .card--split .panel{position:absolute;left:0;top:0;width:237px;height:100%;background:var(--blue);
        box-shadow:3px 0 4px rgba(0,0,0,.15)}
  .name-box{position:absolute;background:var(--black);color:var(--white);padding:15px 17px}
  .name-box__name{font-size:21px;line-height:1.2;font-weight:400}
  .name-box__title{font-size:16px;line-height:1.3;margin-top:3px}
  .card--split .name-box{left:0;top:33px;width:260px;height:74px}
  .fold{position:absolute;width:0;height:0}
  .card--split .fold{left:237px;top:107px;border-top:16px solid #333;border-right:23px solid transparent}
  .card--split .brand{left:278px;top:183px;font-size:19px}

  .contacts{position:absolute;list-style:none;font-size:12px}
  .contacts li{display:flex;align-items:center;gap:9px;height:25px;white-space:nowrap}
  .contacts svg{width:17px;height:17px;flex:none}
  .card--split .contacts{left:275px;top:250px}
  .card--split .contacts svg{fill:var(--blue)}

  /* bars card */
  .card--bars .panel{position:absolute;left:0;top:0;width:259px;height:100%;background:var(--blue)}
  .card--bars .person{position:absolute;left:0;width:259px;top:46px;text-align:center;color:var(--white)}
  .person__name{font-size:28px;font-weight:400}
  .person__title{font-size:16px;margin-top:10px}
  .card--bars .brand{left:284px;top:68px;font-size:18px}
  .bar{position:absolute;left:259px;width:260px;height:42px;background:var(--black);color:var(--white);
       display:flex;align-items:center;padding-left:27px;gap:10px;font-size:12px;white-space:nowrap;
       clip-path:polygon(0 0,100% 0,100% 100%,0 100%,10px 50%)}
  .bar svg{width:17px;height:17px;fill:var(--white);flex:none}
  .bar--phone{top:151px}.bar--post{top:200px}.bar--mail{top:250px}.bar--web{top:299px}

  /* diagonal card */
  .card--diagonal .slab{position:absolute;inset:0;background:var(--blue);
        clip-path:polygon(307px 0,100% 0,100% 100%,190px 100%)}
  .card--diagonal .name-box{left:233px;top:34px;width:286px;height:74px;padding:14px 22px}
  .card--diagonal .fold{left:233px;top:108px;border-top:16px solid #333;border-left:40px solid transparent}
  .card--diagonal .brand{left:19px;top:150px;font-size:18px}
  .card--diagonal .contacts{left:300px;top:248px;color:var(--white)}
  .card--diagonal .contacts svg{fill:var(--white)}

  /* standalone brand */
  .brand--solo{left:705px;top:325px;font-size:34px}

  /* service cards */
  .services-card{position:absolute;left:626px;width:535px;background:var(--white)}
  .services-card--front{top:441px;height:168px;background:var(--blue);border-top:20px solid var(--black)}
  .services-card--back{top:645px;height:370px}
  .services-card--back .blue-field{position:absolute;left:0;top:0;width:100%;height:256px;background:var(--blue)}
  .services-card--back .base-band{position:absolute;left:0;bottom:0;width:100%;height:20px;background:var(--black)}
  .services-card--back .brand{left:122px;top:285px;font-size:26px}

  .services{position:absolute;left:0;width:100%;list-style:none}
  .services-card--front .services{top:30px}
  .services-card--back .services{top:160px}
  .service{position:absolute;top:0;width:110px;margin-left:-55px;text-align:center;color:var(--white);font-size:12px}
  .service__photo{display:block;width:67px;height:67px;margin:0 auto 8px;border-radius:50%;
        border:3px solid #111;background:radial-gradient(circle at 40% 35%,#8aa3b8,#3d4a55)}
  .service--scaffold{left:61px}.service--rigging{left:157px}.service--hoists{left:268px}
  .service--swing{left:377px}.service--labour{left:472px}
  .service--rigging .service__photo{background:radial-gradient(circle at 40% 40%,#d9a0b0,#5a3a40)}
  .service--hoists .service__photo{background:radial-gradient(circle at 50% 60%,#d9922e,#5f9bd0 60%)}
  .service--labour .service__photo{background:radial-gradient(circle at 60% 35%,#f0d040,#5a5a40 70%)}
</style>
</head>
<body>
<svg class="icon-defs" aria-hidden="true">
  <symbol id="i-phone" viewBox="0 0 24 24"><path d="M12 1a11 11 0 1 0 0 22 11 11 0 0 0 0-22zm0 2a9 9 0 1 1 0 18 9 9 0 0 1 0-18z"/><path d="M8.2 6.5l1.9-.4 1.1 2.8-1.3 1c.6 1.4 1.6 2.5 3 3.2l1.1-1.2 2.8 1.2-.5 1.9c-4.4.2-8.5-3.9-8.1-8.5z"/></symbol>
  <symbol id="i-pin" viewBox="0 0 24 24"><path d="M12 1a7.5 7.5 0 0 0-7.5 7.5C4.5 14 12 23 12 23s7.5-9 7.5-14.5A7.5 7.5 0 0 0 12 1zm0 10.5a3 3 0 1 1 0-6 3 3 0 0 1 0 6z"/></symbol>
  <symbol id="i-mail" viewBox="0 0 24 24"><path d="M1 5h22v14H1zm2 2v.3l9 6.2 9-6.2V7zm0 2.7V17h18V9.7l-9 6.1z"/></symbol>
  <symbol id="i-web" viewBox="0 0 24 24"><path d="M12 1a11 11 0 1 0 0 22 11 11 0 0 0 0-22zm-1 2.1V7H7.6C8.3 5 9.5 3.5 11 3.1zm2 0c1.5.4 2.7 1.9 3.4 3.9H13zM5.6 7H3.9a9 9 0 0 1 3.6-3.3A10 10 0 0 0 5.6 7zm12.8 0a10 10 0 0 0-1.9-3.3A9 9 0 0 1 20.1 7zM3.1 9h2.1a15 15 0 0 0 0 6H3.1a9 9 0 0 1 0-6zm4.1 0H11v6H7.2a13 13 0 0 1 0-6zM13 9h3.8a13 13 0 0 1 0 6H13zm5.8 0h2.1a9 9 0 0 1 0 6h-2.1a15 15 0 0 0 0-6zM3.9 17h1.7a10 10 0 0 0 1.9 3.3A9 9 0 0 1 3.9 17zm3.7 0H11v3.9c-1.5-.4-2.7-1.9-3.4-3.9zM13 17h3.4c-.7 2-1.9 3.5-3.4 3.9zm5.4 0h1.7a9 9 0 0 1-3.6 3.3 10 10 0 0 0 1.9-3.3z"/></symbol>
</svg>

<section class="card card--split">
  <div class="panel"></div>
  <div class="name-box"><p class="name-box__name">OWEN PELLEW</p><p class="name-box__title">DIRECTOR</p></div>
  <div class="fold"></div>
  <div class="brand"><span class="brand__mark"></span><span class="brand__name">Firm Deck Hoisting</span></div>
  <ul class="contacts">
    <li><svg><use href="#i-phone"/></svg>0491 572 864</li>
    <li><svg><use href="#i-pin"/></svg>PO BOX 3251, Elmsvale SA 5190</li>
    <li><svg><use href="#i-mail"/></svg>owen@firmdeckhoisting.com.au</li>
    <li><svg><use href="#i-web"/></svg>www.firmdeckhoisting.com.au</li>
  </ul>
</section>

<section class="card card--bars">
  <div class="panel"></div>
  <div class="person"><p class="person__name">OWEN PELLEW</p><p class="person__title">DIRECTOR</p></div>
  <div class="brand"><span class="brand__mark"></span><span class="brand__name">Firm Deck Hoisting</span></div>
  <div class="bar bar--phone"><svg><use href="#i-phone"/></svg>0491 572 864</div>
  <div class="bar bar--post"><svg><use href="#i-pin"/></svg>PO BOX 3251, Elmsvale SA 5190</div>
  <div class="bar bar--mail"><svg><use href="#i-mail"/></svg>owen@firmdeckhoisting.com.au</div>
  <div class="bar bar--web"><svg><use href="#i-web"/></svg>www.firmdeckhoisting.com.au</div>
</section>

<section class="card card--diagonal">
  <div class="slab"></div>
  <div class="name-box"><p class="name-box__name">OWEN PELLEW</p><p class="name-box__title">DIRECTOR</p></div>
  <div class="fold"></div>
  <div class="brand"><span class="brand__mark"></span><span class="brand__name">Firm Deck Hoisting</span></div>
  <ul class="contacts">
    <li><svg><use href="#i-phone"/></svg>0491 572 864</li>
    <li><svg><use href="#i-pin"/></svg>PO BOX 3251, Elmsvale SA 5190</li>
    <li><svg><use href="#i-mail"/></svg>owen@firmdeckhoisting.com.au</li>
    <li><svg><use href="#i-web"/></svg>www.firmdeckhoisting.com.au</li>
  </ul>
</section>

<div class="brand brand--solo"><span class="brand__mark"></span><span class="brand__name">Firm Deck Hoisting</span></div>

<section class="services-card services-card--front">
  <ul class="services">
    <li class="service service--scaffold"><span class="service__photo" role="img" aria-label="Photo of scaffolding on a building"></span>Scaffolding</li>
    <li class="service service--rigging"><span class="service__photo" role="img" aria-label="Photo of rigging shackles"></span>Rigging</li>
    <li class="service service--hoists"><span class="service__photo" role="img" aria-label="Photo of a material hoist bucket against the sky"></span>Man material hoists</li>
    <li class="service service--swing"><span class="service__photo" role="img" aria-label="Photo of a swing stage on a facade"></span>Swing stages</li>
    <li class="service service--labour"><span class="service__photo" role="img" aria-label="Photo of a worker in a hard hat"></span>Labour hire</li>
  </ul>
</section>

<section class="services-card services-card--back">
  <div class="blue-field"></div>
  <ul class="services">
    <li class="service service--scaffold"><span class="service__photo" role="img" aria-label="Photo of scaffolding on a building"></span>Scaffolding</li>
    <li class="service service--rigging"><span class="service__photo" role="img" aria-label="Photo of rigging shackles"></span>Rigging</li>
    <li class="service service--hoists"><span class="service__photo" role="img" aria-label="Photo of a material hoist bucket against the sky"></span>Man material hoists</li>
    <li class="service service--swing"><span class="service__photo" role="img" aria-label="Photo of a swing stage on a facade"></span>Swing stages</li>
    <li class="service service--labour"><span class="service__photo" role="img" aria-label="Photo of a worker in a hard hat"></span>Labour hire</li>
  </ul>
  <div class="brand"><span class="brand__mark"></span><span class="brand__name">Firm Deck Hoisting</span></div>
  <div class="base-band"></div>
</section>
</body>
</html>
```